Acupuncture Medspa needs a business card design

I need a business card design that looks professional, has a spa-like quality and can offer a promo on the back. Initial promo is "First session free". The tagline of NeedleNook is: Refresh, Restore, Rejuvenate.

NeedleNook is a membership-based acupuncture medspa that offers acupuncture, cupping, and herbal therapies. Members choose between the "Refresh" membership which is for stress relief, or "Restore" which is for treating health conditions, and lastly "Rejuvenate" which is for natural facial enhancement.

Industry/Entity Type

Health And Wellness

Contact Information for Business Card

Coral Haskins, MAC, L.Ac.
612-555-0193
www.needlenook-example.com

Font styles to use
Serif
Sans Serif

Colors

Designer to choose colors to be used in the design.

Requirements
Must have
• The project must have NeedleNook logo, promo on the back, and contact information
Nice to have
• I would like to see the colors of the logo used.

```html
<!DOCTYPE html>
<html lang="en">
<head>
<meta charset="utf-8">
<title>NeedleNook Business Card</title>
<link rel="stylesheet" href="https://fonts.googleapis.com/css2?family=Montserrat:wght@600&family=Nunito:wght@300;600;700&family=Arimo:wght@700&display=swap">
<style>
  :root {
    --teal: #1a8883;
    --teal-soft: #d3e8e7;
    --teal-glow: #3a9390;
    --ink: #3d2a22;
    --white: #ffffff;
    --frame: #1a8883;
  }
  * { margin: 0; padding: 0; box-sizing: border-box; }
  html, body {
    width: 1000px; height: 1200px; overflow: hidden;
    background: var(--white);
  }
  .sheet { position: relative; width: 1000px; height: 1200px; }

  .card {
    position: absolute; left: 169px; width: 662px; height: 429px; overflow: hidden;
  }
  .card--front { top: 130px; border: 1px solid var(--frame); background: var(--white); }
  .card--back { top: 640px; background: var(--teal); }

  .wordmark {
    position: absolute;
    font-family: "Montserrat", sans-serif;
    font-weight: 600;
    letter-spacing: 0.5px;
    line-height: 1;
  }
  .card--front .wordmark { left: 35px; top: 64px; font-size: 46px; color: var(--teal); }

  .front-accent {
    position: absolute; left: 290px; top: 110px; width: 340px; height: 340px;
  }

  .holder {
    position: absolute; left: 35px; top: 266px;
    font-family: "Nunito", sans-serif; font-weight: 700; font-size: 21px;
    color: var(--ink);
  }
  .contact { position: absolute; left: 42px; list-style: none; }
  .contact li {
    display: flex; align-items: center; gap: 10px;
    font-family: "Arimo", sans-serif; font-weight: 700; color: var(--ink);
    height: 26px;
  }
  .contact { top: 320px; }
  .contact .phone { font-size: 17px; letter-spacing: 2.4px; }
  .contact .web { font-size: 16px; }
  .contact svg { flex: none; }

  .back-accent {
    position: absolute; left: 150px; top: 10px; width: 420px; height: 420px;
  }
  .card--back .wordmark {
    left: 0; right: 0; top: 188px; text-align: center;
    font-size: 50px; color: var(--white);
  }
  .tagline {
    position: absolute; left: 0; right: 0; top: 240px; text-align: center;
    font-family: "Nunito", sans-serif; font-weight: 300; font-size: 25px;
    color: var(--white);
  }
  .promo {
    position: absolute; left: 0; right: 0; top: 383px; text-align: center;
    font-family: "Nunito", sans-serif; font-weight: 300; font-size: 21px;
    letter-spacing: 5.5px; color: var(--white);
  }
</style>
</head>
<body>
<main class="sheet">
  <section class="card card--front" aria-label="Card front">
    <div class="wordmark">NeedleNook</div>
    <svg class="front-accent" viewBox="0 0 340 340" aria-hidden="true">
      <circle cx="170" cy="170" r="165" fill="var(--teal-soft)" opacity="0.7"/>
    </svg>
    <p class="holder">Coral Haskins, MAC, L.Ac.</p>
    <ul class="contact">
      <li class="phone">
        <svg width="26" height="24" viewBox="0 0 26 24" aria-hidden="true">
          <path d="M6 3c1 0 3 4 3 5s-2 2-2 3 3 5 5 6c1 0 2-2 3-2s4 2 4 3-2 4-4 4C9 22 3 14 3 7c0-2 2-4 3-4z" fill="var(--teal)"/>
          <path d="M14 5a6 6 0 0 1 6 6M15 1a10 10 0 0 1 9 9" fill="none" stroke="var(--teal)" stroke-width="1.6" stroke-linecap="round"/>
        </svg>
        612-555-0193
      </li>
      <li class="web">
        <svg width="22" height="16" viewBox="0 0 22 16" aria-hidden="true">
          <rect x="1" y="2" width="20" height="13" fill="none" stroke="var(--teal)" stroke-width="1.8"/>
          <path d="M1 2l10 8 10-8" fill="none" stroke="var(--teal)" stroke-width="1.8"/>
        </svg>
        www.needlenook-example.com
      </li>
    </ul>
  </section>

  <section class="card card--back" aria-label="Card back">
    <svg class="back-accent" viewBox="0 0 420 420" aria-hidden="true">
      <circle cx="210" cy="210" r="205" fill="var(--teal-glow)" opacity="0.8"/>
    </svg>
    <div class="wordmark">NeedleNook</div>
    <p class="tagline">Refresh. Restore. Rejuvenate</p>
    <p class="promo">First Session Free</p>
  </section>
</main>
</body>
</html>
```